BenQoral Medical

We are a medical supplier company we sell machines and equipment to all medical sectors in Iraq. Our services include not only the installation of these machines and equipment but also we provide support after installation and we train the staff to use these machines/equipment
We need a website that will make us stand out from our competitors, something professional and catchy
Starting from the home page, before showing the home page we want the loading screen to have our logo animated in a nice way
Then we can proceed to creating the other pages which are
Projects
Services
Training
About
and Contact us
Attached below is our logo and the color blue that we hope to use in the theme of the website
**** In the home page we want to focus on our partners and services****

Target Market(s)

Medical Sector

Industry/Entity Type

Medical

Coding

Coded - Design and coding required

Number of Pages Required

5+ page

Colors
0054AA
0677BA
7BADD7
CADEEF
E8F1F8

Requirements
Must have
• Animation in loading screen or animation in home page
Nice to have
• Some sort of animation for our partners

```html
<!DOCTYPE html>
<html lang="en">
<head>
<meta charset="utf-8">
<title>BenQoral Medical</title>
<link href="https://fonts.googleapis.com/css2?family=Poppins:wght@400;500;600;700&display=swap" rel="stylesheet">
<style>
:root{
  --navy:#132f83;
  --deep:#1b2a5e;
  --cyan:#3fc6ee;
  --sky:#4bb6e2;
  --hero:#e2f6fc;
  --card1:#e0f6fd;
  --card2:#e6ecfb;
  --card3:#e4e6ea;
  --grey:#e1e5ea;
  --ink:#1d1d1f;
  --white:#ffffff;
}
*{margin:0;padding:0;box-sizing:border-box}
html,body{width:1200px;height:4367px;overflow:hidden}
body{font-family:'Poppins',sans-serif;background:var(--white);color:var(--ink);position:relative}
.abs{position:absolute}
.brand{font-weight:700;color:var(--navy);font-size:24px;display:flex;align-items:center;gap:10px;white-space:nowrap}
.brand i{display:block;width:20px;height:20px;border:3px solid var(--sky)}
.nav{left:0;top:0;width:1200px;height:80px;background:var(--white)}
.nav a{position:absolute;top:26px;font-weight:600;font-size:17px;color:var(--navy);text-decoration:none}
.nav .home{left:390px;top:12px;width:149px;height:52px;border:2px solid var(--navy);border-radius:26px;display:flex;align-items:center;justify-content:center;gap:10px}
.hero{left:0;top:80px;width:1200px;height:508px;background:var(--hero)}
.sale{left:112px;top:155px;font-size:43px;font-weight:700;color:var(--cyan);line-height:1}
.h1{font-weight:700;color:var(--navy);line-height:51px}
.btn{display:flex;align-items:center;justify-content:center;gap:10px;color:var(--white);border-radius:30px;font-weight:500;font-size:13px}
.photo{background:linear-gradient(135deg,#dfe3e6,#b9c0c6 55%,#8a9097)}
.dot{width:16px;height:16px;border-radius:50%;background:var(--navy);top:536px}
.section-title{width:1200px;text-align:center;font-weight:700;color:var(--navy);font-size:38px}
.svc{border:5px solid var(--navy);text-align:center}
.svc h3{font-size:22px;font-weight:500;color:var(--ink)}
.svc p{font-size:17px;line-height:25px;margin:18px auto 0;width:250px}
.svc .icon{margin-top:30px;height:56px}
.svc .btn{width:176px;height:40px;margin:38px auto 0;background:var(--sky);font-size:12px}
.proj{width:310px;height:210px;border:5px solid var(--navy);border-radius:18px 18px 0 0}
.proj .photo{width:100%;height:100%;border-radius:13px 13px 0 0}
.tag{width:280px;height:105px;border-radius:16px;background:var(--navy);color:var(--white);padding:16px 0 0 26px}
.tag.dark{background:#000}
.tag h4{font-size:20px;font-weight:700;letter-spacing:.5px}
.tag p{font-size:11px;line-height:17px;margin-top:2px}
.tag svg{position:absolute;right:26px;top:34px}
.faq{left:222px;width:766px;height:64px;border-bottom:2px solid #c9d1e0;display:flex;align-items:center;justify-content:space-between;font-size:19px;font-weight:500;color:var(--navy)}
.faq span.plus{width:46px;height:36px;background:var(--navy);color:#fff;border-radius:4px;display:flex;align-items:center;justify-content:center;font-size:24px;font-weight:600}
.field{background:#fff;border-radius:22px;font-size:14px;letter-spacing:2px;color:#555;padding:12px 26px}
.foot{color:#fff;font-size:13px}
.foot h5{font-size:13px;font-weight:600}
.soc{width:34px;height:34px;border:2px solid #fff;border-radius:50%;top:4122px}
.ci{width:36px;height:36px;border:2px solid #fff;border-radius:50%;display:flex;align-items:center;justify-content:center}
</style>
</head>
<body>

<header class="abs nav">
  <div class="abs brand" style="left:113px;top:22px"><i></i>BenQoral Medical</div>
  <a class="home" href="#">
    <svg width="30" height="26" viewBox="0 0 30 26" fill="none" stroke="#4bb6e2" stroke-width="2"><rect x="2" y="2" width="26" height="22"/><path d="M9 2v22M2 13h26"/></svg>Home</a>
  <a href="#" style="left:563px">Projects</a>
  <a href="#" style="left:676px">Services</a>
  <a href="#" style="left:790px">Training</a>
  <a href="#" style="left:903px">About</a>
  <a href="#" style="left:997px">Contact us</a>
</header>

<section class="abs hero"></section>
<div class="abs sale">Sale <span style="color:var(--navy)">30%</span> off</div>
<h1 class="abs h1" style="left:112px;top:204px;font-size:45px">Medical Personal<br>protective equipment</h1>
<p class="abs" style="left:112px;top:324px;width:480px;font-size:17px;line-height:28px">When an unknown printer took a galley of type and scrambled it to make a type specimen book. It has survived.</p>
<div class="abs btn" style="left:113px;top:436px;width:206px;height:49px;background:var(--navy);font-size:17px">Read More
  <svg width="38" height="28" viewBox="0 0 38 28" fill="none" stroke="#fff" stroke-width="2"><rect x="2" y="2" width="34" height="24"/><path d="M12 2v24M2 14h34"/></svg></div>
<div class="abs photo" role="img" aria-label="Hospital equipment photograph" style="left:690px;top:164px;width:397px;height:302px"></div>
<svg class="abs" style="left:553px;top:534px" width="14" height="20" viewBox="0 0 14 20"><path d="M11 2 3 10l8 8" fill="none" stroke="#111" stroke-width="2.5"/></svg>
<div class="abs dot" style="left:580px"></div>
<div class="abs dot" style="left:601px"></div>
<div class="abs dot" style="left:623px"></div>
<div class="abs dot" style="left:646px"></div>
<svg class="abs" style="left:678px;top:534px" width="14" height="20" viewBox="0 0 14 20"><path d="M3 2l8 8-8 8" fill="none" stroke="#111" stroke-width="2.5"/></svg>

<section>
  <div class="abs" role="img" aria-label="MRI scanner in a bright hospital room" style="left:0;top:588px;width:619px;height:449px;background:linear-gradient(90deg,#c7d8e6 0%,#dbe6ee 50%,#f4f8fb 85%,#fff 100%)"></div>
  <div class="abs" style="left:590px;top:683px;font-size:13px;color:var(--navy)">FIND OUT ABOUT US</div>
  <h2 class="abs h1" style="left:588px;top:700px;font-size:41px;line-height:46px">Medical Personal<br>protective equipment</h2>
  <div class="abs btn" style="left:590px;top:824px;width:176px;height:40px;background:var(--sky);font-size:12px">
    <svg width="20" height="18" viewBox="0 0 20 18" fill="none" stroke="#fff" stroke-width="1.5"><circle cx="7" cy="5" r="3.5"/><path d="M1 17c0-4 3-6 6-6s6 2 6 6M13 9h6M16 6v6"/></svg>Free Consultation</div>
  <div class="abs btn" style="left:778px;top:824px;width:198px;height:40px;background:var(--navy);font-size:12px">
    <svg width="24" height="18" viewBox="0 0 24 18" fill="none" stroke="#fff" stroke-width="1.5"><circle cx="6" cy="4" r="2.5"/><circle cx="12" cy="4" r="2.5"/><circle cx="18" cy="4" r="2.5"/><path d="M2 17v-5h20v5M8 12v5M16 12v5"/></svg>54000 Happy Clients</div>
  <p class="abs" style="left:590px;top:882px;width:490px;font-size:17px;line-height:28px">Lorem Ipsum is simply dummy text of the printing and typesetting industry. Lorem Ipsum has been the industry's standard dummy text ever since the 1500s, when an unknown printer took.</p>
  <div class="abs btn" style="left:590px;top:1022px;width:176px;height:41px;background:var(--sky);font-size:12px">Explore Service
    <svg width="22" height="22" viewBox="0 0 22 22" fill="none" stroke="#fff" stroke-width="1.6"><circle cx="9" cy="9" r="7"/><path d="M14 14l6 6"/></svg></div>
</section>

<h2 class="abs section-title" style="left:0;top:1140px">Services</h2>

<article class="abs svc" style="left:112px;top:1264px;width:310px;height:411px;background:var(--card1)">
  <svg class="icon" width="56" height="48" viewBox="0 0 56 48" fill="none" stroke="#132f83" stroke-width="2"><rect x="3" y="3" width="50" height="38" rx="3"/><rect x="9" y="9" width="38" height="26"/><path d="M11 24h8l4-9 5 14 4-9h13M20 45h16"/></svg>
  <h3 style="margin-top:16px">Cardio Monitoring</h3>
  <p>Lorem Ipsum is simply dummy text of the printing and typesetting industry. Lorem Ipsum has been the industry's standard dummy text ever since.</p>
  <div class="btn" style="margin-top:28px">Explore Service</div>
</article>
<article class="abs svc" style="left:446px;top:1310px;width:310px;height:412px;background:var(--card2)">
  <svg class="icon" width="60" height="60" viewBox="0 0 60 60" fill="none" stroke="#132f83" stroke-width="2"><rect x="20" y="4" width="22" height="20" rx="3"/><path d="M31 8v12M25 14h12M4 44l10-8h14l10-6c3-2 6 2 3 5L27 48H10"/></svg>
  <h3 style="margin-top:12px">Medical Treatment</h3>
  <p>Lorem Ipsum is simply dummy text of the printing and typesetting industry. Lorem Ipsum has been the industry's standard dummy text ever since.</p>
  <div class="btn" style="margin-top:28px">Explore Service</div>
</article>
<article class="abs svc" style="left:776px;top:1258px;width:311px;height:410px;background:var(--card3)">
  <svg class="icon" width="52" height="56" viewBox="0 0 52 56" fill="none" stroke="#4a6fb0" stroke-width="2"><path d="M8 10c-4 4-4 10 2 18s14 16 22 20c4 2 8 0 10-3l-7-7-5 3c-5-3-10-8-13-13l3-5-7-7z"/><path d="M28 4h18v10c0 5-4 8-9 10-5-2-9-5-9-10z"/><path d="M37 9v9M33 13h8"/></svg>
  <h3 style="margin-top:20px">Emergency Help</h3>
  <p>Lorem Ipsum is simply dummy text of the printing and typesetting industry. Lorem Ipsum has been the industry's standard dummy text ever since.</p>
  <div class="btn" style="margin-top:28px">Explore Service</div>
</article>

<section class="abs" style="left:0;top:1905px;width:1200px;height:802px;background:var(--grey)"></section>
<h2 class="abs section-title" style="left:0;top:1966px">Project</h2>

<div class="abs proj" style="left:112px;top:2053px"><div class="photo" role="img" aria-label="Operating theatre with surgical lights"></div></div>
<div class="abs tag dark" style="left:134px;top:2190px"><h4>PROJECT 01</h4><p>Lorem Ipsum is simply<br>dummy text of the printing</p><svg width="36" height="36" viewBox="0 0 36 36" fill="none" stroke="#fff" stroke-width="4"><path d="M4 32 32 4M12 4h20v20"/></svg></div>
<div class="abs proj" style="left:446px;top:2053px"><div class="photo" role="img" aria-label="Laboratory microscope on a bench"></div></div>
<div class="abs tag" style="left:468px;top:2190px"><h4>PROJECT 01</h4><p>Lorem Ipsum is simply<br>dummy text of the printing</p><svg width="36" height="36" viewBox="0 0 36 36" fill="none" stroke="#fff" stroke-width="4"><path d="M4 32 32 4M12 4h20v20"/></svg></div>
<div class="abs proj" style="left:778px;top:2053px"><div class="photo" role="img" aria-label="Row of anaesthesia machines"></div></div>
<div class="abs tag" style="left:800px;top:2190px"><h4>PROJECT 01</h4><p>Lorem Ipsum is simply<br>dummy text of the printing</p><svg width="36" height="36" viewBox="0 0 36 36" fill="none" stroke="#fff" stroke-width="4"><path d="M4 32 32 4M12 4h20v20"/></svg></div>

<div class="abs proj" style="left:112px;top:2353px"><div class="photo" role="img" aria-label="Technician working with production equipment" style="background:linear-gradient(135deg,#c9d3dc,#8fa6b8 60%,#5e7f99)"></div></div>
<div class="abs tag" style="left:134px;top:2490px"><h4>PROJECT 01</h4><p>Lorem Ipsum is simply<br>dummy text of the printing</p><svg width="36" height="36" viewBox="0 0 36 36" fill="none" stroke="#fff" stroke-width="4"><path d="M4 32 32 4M12 4h20v20"/></svg></div>
<div class="abs proj" style="left:446px;top:2353px"><div class="photo" role="img" aria-label="Clean room staff at work" style="background:linear-gradient(135deg,#dfe9f0,#a8c8dc 60%,#6fa5c4)"></div></div>
<div class="abs tag" style="left:468px;top:2490px"><h4>PROJECT 01</h4><p>Lorem Ipsum is simply<br>dummy text of the printing</p><svg width="36" height="36" viewBox="0 0 36 36" fill="none" stroke="#fff" stroke-width="4"><path d="M4 32 32 4M12 4h20v20"/></svg></div>
<div class="abs proj" style="left:778px;top:2353px"><div class="photo" role="img" aria-label="Intensive care monitors and bed" style="background:linear-gradient(135deg,#eef2f4,#c3d0d8 60%,#8fa7b6)"></div></div>
<div class="abs tag" style="left:800px;top:2490px"><h4>PROJECT 01</h4><p>Lorem Ipsum is simply<br>dummy text of the printing</p><svg width="36" height="36" viewBox="0 0 36 36" fill="none" stroke="#fff" stroke-width="4"><path d="M4 32 32 4M12 4h20v20"/></svg></div>

<div class="abs section-title" style="left:0;top:2795px;font-size:25px;font-weight:600">Get Your Answer</div>
<h2 class="abs section-title" style="left:0;top:2826px;font-size:40px">Frequently Asked Questions</h2>
<p class="abs" style="left:0;top:2893px;width:1200px;text-align:center;font-size:17px;line-height:26px">Get latest news in your inbox. Consectetur adipiscing<br>elitadipiscing elitse ddo eiusmod tempor incididunt</p>

<div class="abs faq" style="top:2983px">Why opt for our medical services for your family?<span class="plus">+</span></div>
<div class="abs faq" style="top:3047px">Why choose our medical for your family?<span class="plus">+</span></div>
<div class="abs faq" style="top:3111px">Why opt for our healthcare services for your family?<span class="plus">+</span></div>
<div class="abs faq" style="top:3176px">Why choose our medical services for your family?<span class="plus">+</span></div>
<div class="abs faq" style="top:3240px;border-bottom:none">Why choose our healthcare for your family?<span class="plus">+</span></div>

<section class="abs" style="left:242px;top:3393px;width:717px;height:446px;background:var(--deep);border:5px solid #3b9ed8"></section>
<h2 class="abs section-title" style="left:0;top:3433px;color:#fff">Get In Touch</h2>
<div class="abs field" style="left:297px;top:3507px;width:295px;height:43px">Name:</div>
<div class="abs field" style="left:607px;top:3507px;width:293px;height:43px">Phone:</div>
<div class="abs field" style="left:297px;top:3573px;width:295px;height:44px">Email:</div>
<div class="abs field" style="left:607px;top:3573px;width:293px;height:44px">Address:</div>
<div class="abs field" style="left:297px;top:3637px;width:606px;height:97px;border-radius:14px">Comments:</div>
<div class="abs btn" style="left:510px;top:3753px;width:176px;height:40px;background:var(--sky);font-size:13px">Submit Now
  <svg width="24" height="24" viewBox="0 0 22 22" fill="none" stroke="#fff" stroke-width="1.6"><circle cx="9" cy="9" r="7"/><path d="M14 14l6 6"/></svg></div>

<footer class="abs" style="left:0;top:3903px;width:1200px;height:464px;background:var(--deep)"></footer>
<div class="abs brand" style="left:113px;top:3998px;color:#fff"><i style="border-color:#fff"></i>BenQoral Medical</div>
<p class="abs foot" style="left:113px;top:4060px;width:280px;line-height:24px">Lorem Ipsum is simply dummy text of the printing and typesetting</p>
<div class="abs soc" style="left:113px"></div>
<div class="abs soc" style="left:158px"></div>
<div class="abs soc" style="left:203px"></div>
<div class="abs soc" style="left:249px"></div>
<div class="abs soc" style="left:295px"></div>

<div class="abs foot" style="left:436px;top:3978px"><h5>Sitemap</h5></div>
<div class="abs foot" style="left:436px;top:4018px;line-height:34px">Home<br>Projects<br>Services<br>Training<br>About<br>Contact us</div>

<div class="abs foot" style="left:593px;top:3978px"><h5>Contact Us</h5></div>
<div class="abs ci" style="left:592px;top:4016px"><svg width="14" height="18" viewBox="0 0 14 18" fill="none" stroke="#fff" stroke-width="1.8"><path d="M7 17S1 10 1 6.5a6 6 0 0 1 12 0C13 10 7 17 7 17z"/><circle cx="7" cy="6.5" r="2"/></svg></div>
<div class="abs foot" style="left:642px;top:4020px;line-height:17px">48 Cedar Lane, Harbor<br>District 2041</div>
<div class="abs ci" style="left:592px;top:4070px"><svg width="18" height="14" viewBox="0 0 18 14" fill="none" stroke="#fff" stroke-width="1.6"><rect x="1" y="1" width="16" height="12"/><path d="M1 1l8 7 8-7"/></svg></div>
<div class="abs foot" style="left:642px;top:4079px">hello@benqoral.test</div>
<div class="abs ci" style="left:592px;top:4121px"><svg width="16" height="16" viewBox="0 0 16 16" fill="none" stroke="#fff" stroke-width="1.6"><path d="M3 1c-2 2-2 5 1 8s6 5 8 5l2-2-3-3-2 1C7 9 6 8 5 6l1-2-3-3z"/></svg></div>
<div class="abs foot" style="left:642px;top:4130px">+1 (555) 010-4477</div>

<div class="abs foot" style="left:849px;top:3977px"><h5>Sign up to receive the latest news</h5></div>
<p class="abs foot" style="left:849px;top:4015px;line-height:17px">Follow our newsletter to stay<br>updated about us.</p>
<div class="abs" style="left:851px;top:4065px;width:188px;height:45px;background:#fff;font-size:12px;color:#444;padding:14px 14px">Enter your email id:</div>
<div class="abs" style="left:1039px;top:4065px;width:48px;height:45px;background:#139fe0;display:flex;align-items:center;justify-content:center"><svg width="18" height="12" viewBox="0 0 18 12" fill="none" stroke="#fff" stroke-width="2"><path d="M1 6h15M11 1l5 5-5 5"/></svg></div>

<div class="abs" style="left:0;top:4260px;width:1200px;height:1px;background:#3a4a7c"></div>
<div class="abs foot" style="left:0;top:4289px;width:1200px;text-align:center;font-size:15px;font-weight:500">Copyright 2024 . All Rights Reserved</div>

</body>
</html>
```